IT support company needs Banner Ad for the top of their quote layout template

We need a banner Ad for the top of our for quote layout template so it is sent out on all our quotes

The banner size must be 827 x 100 pixels - anything larger than 60 KB can cause upload time issues

We have attached our logo and examples of the quote page to see how it looks in the context of the whole page.

Essential elements of the banner
- Must have our logo but this can be changed to be different colours if it makes the design work better i.e. Tidal Grove could be all in white

Colours
- Can use all of our standard colours - Orange, Black, Grey and White

Images
- As a premium IT support company we deal with people and technology so would like to see both of these Incorporated into the banner i.e. people using technology These images could be watermarked or one colour effect.

Look and Feel
- Professional, friendly, people, technology, premium

Target Market
Small business owners and managers

Industry/Entity Type

It Company

```html
<!DOCTYPE html>
<html lang="en">
<head>
<meta charset="UTF-8">
<title>Tidal Grove – Quote Banner</title>
<link href="https://fonts.googleapis.com/css2?family=Montserrat:wght@800&family=Open+Sans:wght@600;700&display=swap" rel="stylesheet">
<style>
  :root {
    --bg-dark: #141518;
    --bg-dark-2: #1d1f23;
    --orange: #f07a1e;
    --orange-deep: #d9620f;
    --white: #ffffff;
    --button-blue: #1f7cc6;
    --photo-light: #dfe8ef;
    --photo-mid: #9fb3c2;
    --photo-dark: #4a5866;
  }
  html, body {
    margin: 0;
    padding: 0;
    overflow: hidden;
    background: var(--bg-dark);
  }
  .banner {
    position: relative;
    width: 1200px;
    height: 145px;
    overflow: hidden;
    background: linear-gradient(90deg, var(--bg-dark) 0%, var(--bg-dark-2) 50%, var(--bg-dark) 100%);
  }
  .banner-art {
    position: absolute;
    inset: 0;
  }
  .brand {
    position: absolute;
    left: 14px;
    top: 50px;
    display: flex;
    align-items: center;
    gap: 10px;
  }
  .brand-dot {
    width: 14px;
    height: 14px;
    border-radius: 50%;
    background: var(--white);
  }
  .brand-name {
    font-family: "Montserrat", sans-serif;
    font-weight: 800;
    font-size: 40px;
    letter-spacing: -0.5px;
    color: var(--white);
    line-height: 1;
    text-transform: uppercase;
  }
  .offer {
    position: absolute;
    right: 18px;
    top: 52px;
    width: 320px;
    text-align: center;
  }
  .offer-text {
    margin: 0;
    font-family: "Open Sans", sans-serif;
    font-weight: 600;
    font-size: 23px;
    color: var(--white);
    line-height: 1;
    white-space: nowrap;
  }
  .cta-button {
    display: inline-flex;
    align-items: center;
    gap: 8px;
    margin-top: 15px;
    padding: 0 16px;
    height: 31px;
    background: var(--button-blue);
    color: var(--white);
    font-family: "Open Sans", sans-serif;
    font-weight: 700;
    font-size: 15px;
    text-transform: uppercase;
    text-decoration: none;
  }
  .cta-arrow {
    width: 0;
    height: 0;
    border-left: 8px solid var(--orange);
    border-top: 6px solid transparent;
    border-bottom: 6px solid transparent;
  }
</style>
</head>
<body>
  <div class="banner">
    <svg class="banner-art" width="1200" height="145" viewBox="0 0 1200 145">
      <defs>
        <linearGradient id="photoTone" x1="0" y1="0" x2="1" y2="0.4">
          <stop offset="0" stop-color="var(--photo-dark)"/>
          <stop offset="0.35" stop-color="var(--photo-mid)"/>
          <stop offset="0.7" stop-color="var(--photo-light)"/>
          <stop offset="1" stop-color="var(--photo-mid)"/>
        </linearGradient>
      </defs>
      <polygon class="photo-area" points="390,0 875,0 795,145 250,145" fill="url(#photoTone)"
               role="img" aria-label="Photo of a person at a desk using a tablet in front of computer monitors"/>
      <polygon class="accent-left" points="385,0 440,0 375,60 340,60" fill="var(--orange)"/>
      <polygon class="accent-right" points="858,0 930,0 830,145 792,145" fill="var(--orange)"/>
      <polygon class="accent-right-shade" points="905,0 930,0 830,145 815,145" fill="var(--orange-deep)"/>
    </svg>

    <div class="brand">
      <span class="brand-name">Tidal Grove</span>
      <span class="brand-dot"></span>
    </div>

    <div class="offer">
      <p class="offer-text">A small text will go here</p>
      <a class="cta-button" href="#">Click here <span class="cta-arrow"></span></a>
    </div>
  </div>
</body>
</html>
```